Graphic to show easy steps to find financial clarity

Howdy-I need a graphic that describe my Coin Compass Method.The attached is a concept, but please use your own creativity to show how you would display this:- There are 5 steps the process (and then we repeat/recalculate)- And three bullets that drive home the results of the processI've also attached my logo. Please use the colors in my logo and maybe add a soft green as needed.The reader should be able to briefly scan this document and understand that this is an easy/simple process that tells them how to manage their cash.Thanks!-Ned

Target Market(s)

wealthy women, whether single or married

Requirements
Must have
• Please use the colors in my logo and a soft green if needed
Should not have
• This should be a very easy to read graphic that communicates how simple/easy this is to do.

```html
<!DOCTYPE html>
<html lang="en">
<head>
<meta charset="utf-8">
<title>Coin Compass Method</title>
<link rel="stylesheet" href="https://fonts.googleapis.com/css2?family=Playfair+Display:wght@400&family=Montserrat:wght@400;500;700;800&display=swap">
<style>
  :root {
    --navy: #1b3a78;
    --cyan: #00aeef;
    --cyan-deep: #0b8fd0;
    --bar: #e6e6e7;
    --ink: #1e1e1e;
    --text: #2b3a55;
    --paper: #ffffff;
  }
  * { box-sizing: border-box; margin: 0; padding: 0; }
  html, body { width: 1200px; height: 1004px; overflow: hidden; background: var(--paper); }
  .canvas { position: relative; width: 1200px; height: 1004px; font-family: "Montserrat", sans-serif; }

  .title {
    position: absolute; right: 75px; top: 62px;
    font-family: "Playfair Display", serif; font-weight: 400;
    font-size: 88px; line-height: 114px; color: var(--ink); text-align: right;
    white-space: nowrap;
  }

  .stack-art {
    position: absolute; left: 150px; top: 238px; width: 292px; height: 452px;
    border-radius: 50% / 22%;
    background: linear-gradient(90deg, #8d8f94 0%, #e9eaec 45%, #a5a7ab 70%, #2f5fa3 100%);
    opacity: .9;
  }

  .arrows { position: absolute; left: 0; top: 0; }

  .steps { position: absolute; left: 378px; top: 306px; list-style: none; }
  .step { display: flex; align-items: center; height: 50px; margin-bottom: 5.5px; }
  .step-bar {
    background: var(--bar); height: 50px; display: flex; align-items: center;
    padding-left: 24px; font-size: 22px; font-weight: 400; color: var(--text); letter-spacing: .3px;
  }
  .step-tag { margin-left: 18px; font-size: 25px; font-weight: 800; color: var(--navy); }

  .results { position: absolute; left: 390px; top: 676px; display: flex; }
  .result { width: 238px; text-align: center; }
  .result-icon {
    width: 130px; height: 130px; margin: 0 auto; border-radius: 50%;
    background: var(--cyan); display: flex; align-items: center; justify-content: center;
  }
  .result-title { font-size: 44px; font-weight: 800; color: var(--cyan); line-height: 52px; margin-top: 6px; }
  .result-text { font-size: 18px; font-weight: 500; color: var(--ink); line-height: 24px; margin: 0 auto; width: 184px; }

  .brand { position: absolute; left: 46px; top: 912px; display: flex; align-items: center; gap: 12px; }
  .brand-mark { width: 30px; height: 30px; background: var(--navy); }
  .brand-name { font-size: 17px; font-weight: 700; color: var(--navy); letter-spacing: .5px; white-space: nowrap; }
</style>
</head>
<body>
<div class="canvas">
  <h1 class="title">Coin Compass<br>Method</h1>

  <div class="stack-art" role="img" aria-label="3D stacked cylinder of rising blue and grey rings"></div>

  <svg class="arrows" width="1200" height="1004" viewBox="0 0 1200 1004" aria-hidden="true">
    <path d="M410 182 C330 120 250 120 205 178" fill="none" stroke="var(--cyan)" stroke-width="26"/>
    <polygon points="172,266 170,170 238,190" fill="var(--cyan-deep)"/>
    <path d="M150 722 C200 790 270 800 340 770" fill="none" stroke="var(--cyan)" stroke-width="26"/>
    <polygon points="412,745 330,735 355,800" fill="var(--cyan-deep)"/>
  </svg>

  <ol class="steps">
    <li class="step"><span class="step-bar" style="width:298px">Recalculate monthly</span><span class="step-tag">Repeat</span></li>
    <li class="step"><span class="step-bar" style="width:348px">Invest the rest</span><span class="step-tag">Step 5</span></li>
    <li class="step"><span class="step-bar" style="width:398px">Save them aside in savings</span><span class="step-tag">Step 4</span></li>
    <li class="step"><span class="step-bar" style="width:448px">Add up your 5-year cash needs</span><span class="step-tag">Step 3</span></li>
    <li class="step"><span class="step-bar" style="width:498px">Project special expenses</span><span class="step-tag">Step 2</span></li>
    <li class="step"><span class="step-bar" style="width:546px">Know your annual spendings</span><span class="step-tag">Step 1</span></li>
  </ol>

  <div class="results">
    <div class="result">
      <div class="result-icon">
        <svg width="70" height="60" viewBox="0 0 70 60" fill="none" stroke="#fff" stroke-width="2.5" stroke-linejoin="round">
          <polygon points="15,8 55,8 66,22 35,56 4,22"/>
          <polyline points="4,22 66,22"/><polyline points="25,8 20,22 35,56 50,22 45,8"/>
        </svg>
      </div>
      <div class="result-title">Know</div>
      <p class="result-text">your lifestyle will be unaffected by the markets for at least 5 years</p>
    </div>
    <div class="result">
      <div class="result-icon">
        <svg width="66" height="66" viewBox="0 0 66 66" fill="none" stroke="#fff" stroke-width="2.5" stroke-linejoin="round">
          <rect x="26" y="18" width="34" height="42"/><path d="M35 18 v-6 a8 8 0 0 1 16 0 v6"/>
          <rect x="6" y="36" width="26" height="24" fill="var(--cyan)"/><line x1="19" y1="36" x2="19" y2="60"/><line x1="4" y1="36" x2="34" y2="36"/>
        </svg>
      </div>
      <div class="result-title">Spend</div>
      <p class="result-text">intentionally and with joy</p>
    </div>
    <div class="result">
      <div class="result-icon">
        <svg width="70" height="66" viewBox="0 0 70 66" fill="none" stroke="#fff" stroke-width="2.5">
          <ellipse cx="28" cy="12" rx="20" ry="6"/><path d="M8 12 v30 a20 6 0 0 0 40 0 v-30"/>
          <path d="M8 22 a20 6 0 0 0 40 0 M8 32 a20 6 0 0 0 40 0"/>
          <circle cx="48" cy="44" r="16" fill="var(--cyan)"/><text x="48" y="51" fill="#fff" stroke="none" font-size="20" font-family="Montserrat, sans-serif" font-weight="700" text-anchor="middle">$</text>
        </svg>
      </div>
      <div class="result-title">Create</div>
      <p class="result-text">a solid base for lifetime cash flow projections</p>
    </div>
  </div>

  <div class="brand">
    <span class="brand-mark"></span>
    <span class="brand-name">HARBOR LANE ADVISORS</span>
  </div>
</div>
</body>
</html>
```